www.brevatin.com Sales/Order Page ReDesign

We need a new and amazing design for our sales/order page to attract more costumers and new houses for our portal.

Here is the existing page with the current design: https://www.brevatin.com/sales

We are proud owners of www.sommarhytta.no and www.brevatin.com and we want more holiday home owners to join our page so that we can rent out their holiday homes and increase the number of houses on our portal.

To get more homeowners we need a sales page that can sell our products the best way possible. Therefore we want you too blow us away with a fresh, modern, easy understandable and stylish new sales/order page.

The only restrictions we give when it comes to design is that it needs to fit the existing design of our portals, the top and footer are set. Beside that we are open for everything as long as it at once give the customers impression that this is a good, professional page were they just have to put out their houses.

When it comes to content I have added two documents who include the content to put in here and some guidelines on how to organize the page. Please be creative and add necessary graphics, symbols, background pictures and what ever necessary to make this page look professional and appealing to new costumers.

Looking forward to what suggestions we are given.

We just want to inform that we have updated our brief with a much more concrete description of what content to add on the sale page, and who to structure the content on the page. Hope this helps to make suggestions easier. Looking forward to receive some good contributions.

We would just like to make sure that everyone have understood that we are not asking for a new design suggestion to our portal in general. We are only asking for a redesign of our sales/order page you find here www.brevatin.com/sales. We have to day received some designs for our front page and the design it self was good, but that's not what we are asking for this time and don't want you to use time of something we don't need at the moment. We are looking forward too se some good suggestions.

Reason: Hello. Thanks for all the great contributions we have been given so fare. We haven't been able to respond to all design and are therefore extending the deadline so that we are able to respond to the designs we have been giver and to gov time to make final changes.

Reason: We are extending the deadline to give designers time to give new suggestion based on our latest feedback today.

Reason: Extended so we can receive last design changes.

Target Market(s)

This is a presentation page where we present our product agains new home owner who we what to choose listing there property on or site.

Industry/Entity Type

Sales

Requirements
Must have
• A modern design who calms the costumer down and help them in deciding to chose us, and for them to choose us they need to trust and believe in us. Therefore your main task is to create a page that effectively informs about our product, gets the visitors attentions and make them trust us.
Nice to have
• Examples of good competitors and good order pages we like:

http://www.cabinquest.example/info/lyp?icid=IL___O_Text___top_nav_link
https://www.nestlodge.example/rooms/new
https://www.pearvix.example/phone/compare/
http://www.guestnook.example/host
Should not have
• - Bad design :-). With bad design we mean design that looks like it's made in 2 seconds by a little child.

```html
<!DOCTYPE html>
<html lang="en">
<head>
<meta charset="utf-8">
<title>Brevatin Holiday Rental – List your property</title>
<link href="https://fonts.googleapis.com/css2?family=Cinzel:wght@400;700&family=Arimo:wght@400;700&display=swap" rel="stylesheet">
<style>
:root{
  --blue:#0a8fd8;
  --blue-dark:#0779b8;
  --panel-blue:#0a85c6;
  --text:#333;
  --muted:#555;
  --heading:#1d8fcf;
  --green:#6cc13f;
  --green-dark:#4fa327;
  --orange:#f7b928;
  --orange-dark:#eea116;
  --footer:#404040;
  --footer-bottom:#2f2f2f;
  --footer-text:#cfcfcf;
  --line:#e3e3e3;
}
*{box-sizing:border-box;margin:0;padding:0}
html,body{width:1200px;height:2667px;overflow:hidden;background:#fff}
body{font-family:"Arimo",Arial,sans-serif;color:var(--text);position:relative}
.abs{position:absolute}

/* top bar */
.topbar{left:0;top:0;width:1200px;height:32px;background:var(--blue);color:#fff;font-size:12px}
.topbar .follow{left:172px;top:9px;display:flex;align-items:center;gap:14px}
.social{width:11px;height:11px;border-radius:50%;background:#fff;opacity:.9;display:inline-block}
.topbar .links{left:745px;top:9px;display:flex;gap:22px}
.lang{left:934px;top:4px;width:95px;height:23px;border:1px solid #fff;font-size:11px;padding:5px 8px;display:flex;align-items:center;gap:6px}
.lang .flag{width:16px;height:10px;background:#fff}

/* header */
.header{left:0;top:32px;width:1200px;height:80px;border-bottom:1px solid var(--line)}
.brand{left:172px;top:22px;display:flex;align-items:center;gap:10px}
.brand .mark{width:30px;height:30px;background:var(--blue)}
.brand .name{font-family:"Cinzel",serif;font-size:30px;color:var(--heading);line-height:1}
.nav{left:519px;top:30px;display:flex;gap:0;font-size:13px;color:#555}
.nav a{display:block;text-decoration:none;color:inherit;padding:6px 0;width:90px;text-align:center;margin-right:50px}
.nav a.active{background:var(--blue);color:#fff;width:74px;border-radius:3px}
.nav a:nth-child(2){width:70px;margin-right:48px}
.nav a:nth-child(3){width:64px;margin-right:46px}
.nav a:nth-child(4){width:68px;margin-right:54px}
.nav a:nth-child(5){width:70px;margin-right:0}

.count{right:172px;top:128px;font-size:12px;font-weight:700;color:var(--heading);display:flex;align-items:center;gap:8px}
.count .house{width:14px;height:14px}

/* hero */
.hero{left:171px;top:158px;width:857px;height:400px;background:linear-gradient(180deg,#2b3a55 0%,#3d4a63 45%,#8a5a2a 70%,#2c4b6a 100%)}
.hero-panel{left:0;top:0;width:267px;height:400px;background:rgba(18,24,32,.88);color:#fff;padding:52px 34px 0 34px}
.hero-panel h2{font-family:"Cinzel",serif;font-weight:400;font-size:22px;line-height:27px}
.hero-panel .lead{font-size:13px;line-height:22px;margin-top:14px}
.hero-panel p{font-size:11px;line-height:22px;margin-top:14px}
.hero-dots{left:36px;top:340px;display:flex;gap:2px}
.hero-dots span{width:22px;height:22px;background:#555}

.intro-title{left:0;top:594px;width:1200px;text-align:center;font-family:"Cinzel",serif;font-size:30px;color:var(--heading)}
.intro-sub{left:0;top:640px;width:1200px;text-align:center;font-size:18px;color:#333}

.section-title{font-family:"Cinzel",serif;font-size:20px;color:var(--heading);left:171px}
.pager{left:998px;top:706px;display:flex;gap:2px}
.pager span{width:14px;height:14px;background:#d5d5d5}

.types{left:171px;top:747px;width:857px;display:flex;justify-content:space-between}
.type{width:190px;height:160px;position:relative}
.type .caption{position:absolute;left:0;bottom:0;width:100%;height:34px;background:rgba(0,0,0,.55);color:#fff;font-size:13px;padding:10px 12px}
.t-villa{background:linear-gradient(180deg,#2a3545,#7a5a3a 60%,#2a2a2a)}
.t-castle{background:linear-gradient(180deg,#c9d6e6,#8a7a68 55%,#5d6a3e)}
.t-apartment{background:linear-gradient(180deg,#2b6fc3,#b9cde3 50%,#4d7a4a)}
.t-farm{background:linear-gradient(180deg,#5d8fbf,#8a4a3a 45%,#4e8c32)}

/* features */
.features{left:171px;top:1022px;width:857px;display:grid;grid-template-columns:300px 306px 251px}
.feature{height:181px}
.feature:nth-child(n+7){height:145px}
.feature:nth-child(n+10){height:140px}
.feature h3{display:flex;align-items:center;gap:10px;font-size:14px;font-weight:400;color:var(--heading);margin-bottom:12px}
.feature .ico{width:28px;height:28px;flex:none}
.feature p{font-size:10.5px;line-height:20px;color:var(--muted);width:250px}

.divider{left:200px;top:1671px;width:800px;height:6px;background:radial-gradient(ellipse at center,rgba(0,0,0,.18),rgba(0,0,0,0) 70%)}

.choose{left:0;top:1720px;width:1200px;text-align:center;font-size:21px;color:var(--heading)}
.btn{height:59px;font-size:11.5px;font-weight:700;color:#fff;text-transform:uppercase;display:flex;align-items:center;justify-content:center;border-radius:2px}
.btn-green{left:171px;top:1778px;width:401px;background:linear-gradient(180deg,#7fd24e,var(--green-dark));border:1px solid var(--green-dark)}
.btn-orange{left:590px;top:1778px;width:402px;background:linear-gradient(180deg,#fbc945,var(--orange-dark));border:1px solid var(--orange-dark)}

/* form */
.offer{left:171px;top:1886px;width:857px;height:333px;background:var(--panel-blue);color:#fff}
.offer h4{position:absolute;left:0;top:34px;width:100%;text-align:center;font-size:17px;font-weight:400}
.field{position:absolute;width:240px}
.field label{display:block;font-size:10.5px;margin-bottom:9px}
.field span{display:block;height:34px;background:#fff;border-radius:3px}
.submit{position:absolute;left:567px;top:246px;width:240px;height:44px;background:linear-gradient(180deg,#fbc945,var(--orange-dark));border-radius:2px;font-size:14px;font-weight:700;display:flex;align-items:center;justify-content:center;text-transform:uppercase}

/* partners */
.partner-a{left:352px;top:2258px;display:flex;align-items:center;gap:10px}
.partner-a .sq{width:54px;height:54px;border-radius:12px;background:#0a5fad}
.partner-a .nm{font-size:30px;font-weight:700;color:#0a5fad}
.partner-b{left:613px;top:2263px;display:flex;align-items:center;gap:10px}
.partner-b .sq{width:40px;height:40px;background:#2a8ad0}
.partner-b .nm{font-size:28px;font-weight:700;color:#2a8ad0}

/* footer */
.footer{left:0;top:2347px;width:1200px;height:270px;background:var(--footer);color:var(--footer-text);font-size:10.5px}
.fcol{position:absolute;top:38px}
.fcol h5{font-size:11px;font-weight:700;color:#fff;text-transform:uppercase;margin-bottom:14px}
.fcol li{list-style:none;line-height:22px}
.worldmap{position:absolute;left:276px;top:74px;width:236px;height:100px;background:radial-gradient(ellipse at 45% 45%,#fafafa 0%,#e6e6e6 55%,rgba(230,230,230,0) 72%)}
.contact li{display:flex;align-items:center;gap:10px}
.contact .ci{width:10px;height:10px;border-radius:50%;background:#9a9a9a}
.contact .sub{font-weight:700;text-transform:uppercase;color:var(--footer-text);margin:6px 0 2px}
.bottombar{left:0;top:2617px;width:1200px;height:50px;background:var(--footer-bottom);color:#bbb;font-size:10.5px;text-align:center;padding-top:18px}
</style>
</head>
<body>

<div class="abs topbar">
  <div class="abs follow">Follow Us :
    <span class="social"></span><span class="social"></span><span class="social"></span><span class="social"></span><span class="social"></span>
  </div>
  <div class="abs links"><span>List your property</span><span>|</span><span>Sign in</span></div>
  <div class="abs lang"><span class="flag"></span>English
    <svg width="8" height="5" viewBox="0 0 8 5" style="margin-left:auto"><path d="M0 0h8L4 5z" fill="#fff"/></svg>
  </div>
</div>

<header class="abs header">
  <div class="abs brand"><span class="mark"></span><span class="name">Brevatin</span></div>
  <nav class="abs nav">
    <a class="active">Home</a><a>About us</a><a>Services</a><a>Property</a><a>Contact Us</a>
  </nav>
</header>

<div class="abs count">
  <svg class="house" viewBox="0 0 14 14"><path d="M1 7 7 1l6 6h-2v6H3V7z" fill="#999"/></svg>5+ PROPERTIES
</div>

<section class="abs hero" role="img" aria-label="Photograph of a modern villa with a lit pool at dusk">
  <div class="abs hero-panel">
    <h2>List Your<br>Property Today!</h2>
    <div class="lead">Brevatin helps you make money on your property, starting now…</div>
    <p>Let professionals who know the travel industries handle all yours booking requests. Great result with less work, our professional team will answer all you inquiries, while you spend time with friends, family and enjoy your own holiday.</p>
  </div>
  <div class="abs hero-dots"><span></span><span></span></div>
</section>

<h1 class="abs intro-title">List Your Property Today!</h1>
<div class="abs intro-sub">Brevatin helps you make money on your property, starting now…</div>

<h2 class="abs section-title" style="top:698px">On Brevatin you can rent out:</h2>
<div class="abs pager"><span></span><span></span></div>
<div class="abs types">
  <div class="type t-villa" role="img" aria-label="Photo of a villa at night"><div class="caption">VILLA</div></div>
  <div class="type t-castle" role="img" aria-label="Photo of a stone castle"><div class="caption">CASTLE</div></div>
  <div class="type t-apartment" role="img" aria-label="Photo of an apartment tower"><div class="caption">APARTMENT</div></div>
  <div class="type t-farm" role="img" aria-label="Photo of a farmhouse with fields"><div class="caption">FARM / FARMHOUSE</div></div>
</div>

<h2 class="abs section-title" style="top:965px">All our announcements</h2>

<div class="abs features">
  <div class="feature"><h3><svg class="ico" viewBox="0 0 28 28"><rect x="4" y="4" width="20" height="20" rx="4" fill="#3b4a6b"/></svg>Help from professionals</h3>
    <p>Let professionals who know the travel industries handle all yours booking requests Great result with less work, our professional team will answer all you inquiries, while you spend time with friends, family and enjoy your own holiday.</p></div>
  <div class="feature"><h3><svg class="ico" viewBox="0 0 28 28"><path d="M4 15l6 6L24 6" fill="none" stroke="#6cc13f" stroke-width="4" stroke-linecap="round" stroke-linejoin="round"/></svg>Access Scandinavians</h3>
    <p>Our roots are from Norway, and we have expertise with the Scandinavian market and can help you get tenants from these very travel friendly demographics.</p></div>
  <div class="feature"><h3><svg class="ico" viewBox="0 0 28 28"><path d="M3 14 14 3h11v11L14 25z" fill="#f2a82a"/><circle cx="20" cy="8" r="2" fill="#fff"/></svg>Broad exposure</h3>
    <p>We have been in the market for several years and are promoting your property through the necessary and right channels.</p></div>

  <div class="feature"><h3><svg class="ico" viewBox="0 0 28 28"><path d="M9 12V8a5 5 0 0 1 10 0v4" fill="none" stroke="#c89a2a" stroke-width="3"/><rect x="5" y="12" width="18" height="13" rx="2" fill="#e2b23a"/></svg>Trust &amp; Safety</h3>
    <p>You are still in control of your property. We have the tools to help you accept a booking only if you're 100% comfortable.</p></div>
  <div class="feature"><h3><svg class="ico" viewBox="0 0 28 28"><rect x="2" y="8" width="16" height="12" fill="#e8a632"/><rect x="18" y="12" width="8" height="8" fill="#555"/><circle cx="8" cy="22" r="3" fill="#333"/><circle cx="21" cy="22" r="3" fill="#333"/></svg>No Traveler fees</h3>
    <p>Unlike many other vacation rental booking sites, travel-ers can book vacation rentals without paying any fees to us, maybe one of the reason we have so many returning costumers.</p></div>
  <div class="feature"><h3><svg class="ico" viewBox="0 0 28 28"><rect x="3" y="6" width="22" height="17" rx="2" fill="#c2742e"/></svg>Payments by Brevatin</h3>
    <p>Guests are always carful when it comes to payment. Everybody can feel safe through secure payment with Brevatin. We are responsible for you getting paid.</p></div>

  <div class="feature"><h3><svg class="ico" viewBox="0 0 28 28"><rect x="3" y="5" width="22" height="15" rx="1" fill="#3a7bc8"/><rect x="10" y="21" width="8" height="3" fill="#777"/></svg>Online Booking</h3>
    <p>We simplify the booking process by allowing tenants to send online reservations request, which gives you a 24-hour period to accept or decline their reservation.</p></div>
  <div class="feature"><h3><svg class="ico" viewBox="0 0 28 28"><circle cx="14" cy="14" r="10" fill="#c9c9c9"/><circle cx="14" cy="14" r="4" fill="#fff"/></svg>Easy-to-Use Tools</h3>
    <p>Get access too a very well developed reservation and management tool that helps you keep track of bookings.</p></div>
  <div class="feature"><h3><svg class="ico" viewBox="0 0 28 28"><ellipse cx="14" cy="19" rx="11" ry="5" fill="#9aa0b5"/><path d="M10 18 22 5" stroke="#555" stroke-width="2"/></svg>Unlimited inquiries</h3>
    <p>When you are renting out your property you need inquiries, therefore we have no fees on inquiries for your property.</p></div>

  <div class="feature"><h3><svg class="ico" viewBox="0 0 28 28"><rect x="3" y="7" width="22" height="15" rx="2" fill="#6aa84f"/><rect x="6" y="10" width="16" height="9" fill="#d9b77a"/></svg>Unlimited photos</h3>
    <p>A picture says more then 1000 words, therefore we inspire you too upload as many pictures as possible.</p></div>
  <div class="feature"><h3><svg class="ico" viewBox="0 0 28 28"><rect x="4" y="5" width="20" height="20" rx="2" fill="#f2f2f2" stroke="#bbb"/><rect x="4" y="5" width="20" height="6" fill="#d33"/><text x="14" y="22" font-size="9" text-anchor="middle" fill="#333" font-family="Arimo,sans-serif">29</text></svg>Online calendar</h3>
    <p>Tenants like to know when your property is available straight away, and we let them know that. At the same time you can easily manage your availability.</p></div>
  <div class="feature"><h3><svg class="ico" viewBox="0 0 28 28"><rect x="3" y="12" width="22" height="12" fill="#d9c79a"/><path d="M14 3a5 5 0 0 1 5 5c0 4-5 9-5 9s-5-5-5-9a5 5 0 0 1 5-5z" fill="#d33"/></svg>Map and location</h3>
    <p>Tenants are always wondering where your property is located. Show them through our map and let them know where nearby attractions are.</p></div>
</div>

<div class="abs divider"></div>

<h2 class="abs choose" style="font-weight:400">How do you want to list your property?</h2>
<div class="abs btn btn-green">Save time while we create income on your property</div>
<div class="abs btn btn-orange">Do it yourself</div>

<section class="abs offer">
  <h4>Get discounts if you have more than one property Type in the number of properties :</h4>
  <div class="field" style="left:35px;top:89px"><label>First Name</label><span></span></div>
  <div class="field" style="left:300px;top:89px"><label>Last Name</label><span></span></div>
  <div class="field" style="left:567px;top:89px"><label>Email</label><span></span></div>
  <div class="field" style="left:35px;top:167px"><label>Phone Number</label><span></span></div>
  <div class="field" style="left:300px;top:167px"><label>How they want to be contacted</label><span></span></div>
  <div class="field" style="left:567px;top:167px"><label>When they want to be contacted</label><span></span></div>
  <div class="submit">Conform now</div>
</section>

<div class="abs partner-a"><span class="sq"></span><span class="nm">Kvikk</span></div>
<div class="abs partner-b"><span class="sq"></span><span class="nm">Sommarhytta.no</span></div>

<footer class="abs footer">
  <div class="fcol" style="left:172px"><h5>Destinations</h5>
    <ul><li>Europe</li><li>North America</li><li>South America</li><li>Africa</li><li>Asia</li><li>Australia</li></ul></div>
  <div class="worldmap" role="img" aria-label="World map silhouette"></div>
  <div class="fcol" style="left:516px"><h5>For tenants</h5>
    <ul><li>For tenants</li><li>My page</li><li>Why Brevatin?</li><li>Help</li><li>Rental terms</li></ul></div>
  <div class="fcol" style="left:668px"><h5>For house owners</h5>
    <ul><li>For house owners</li><li>MyAdmin</li><li>Let us rent your house</li><li>Conditions</li></ul></div>
  <div class="fcol contact" style="left:850px"><h5>For house owners</h5>
    <ul>
      <li class="sub">Brevatin Holiday Rental</li>
      <li><span class="ci"></span>post@brevatin.com</li>
      <li><span class="ci"></span>+47 55 01 23 45</li>
      <li><span class="ci"></span>www.brevatin.com</li>
      <li class="sub">Opening hours</li>
      <li><span class="ci"></span>Mon - Fri: 9.00 AM - 5.00 PM</li>
      <li><span class="ci"></span>Sat - Sun: Closed</li>
    </ul></div>
</footer>
<div class="abs bottombar">© 2014. Brevatin. All rights reserved</div>

</body>
</html>
```